Flier advertising books and newsletter

A4 flier advertising my free e-newsletter and two books, as well as an invite to like us on mingleo.

needs to look good in full colour but that can be printed in black and white on the occasions that mass mail outs are required and cost becomes an issue.

Modern, funky but acceptable to corporate. No stock photos of people please.

I have attached the file - there are three pictures - one of each book , and also our logo I can attach the original jpegs when required.

UPDATE: The first couple of designs convinced me that there was too much text in my flier for an a4 document so I have edited the attached document to reduce the amount of text.

```html
<!DOCTYPE html>
<html lang="en">
<head>
<meta charset="utf-8">
<title>Brightpath Psychology – Newsletter and Books Flier, Colour and Mono Editions</title>
<link href="https://fonts.googleapis.com/css2?family=Poppins:ital,wght@0,700;1,800&family=Roboto+Condensed:wght@700&family=Open+Sans:ital,wght@0,400;0,700;1,400&family=Playfair+Display:ital@1&display=swap" rel="stylesheet">
<style>
  :root {
    --canvas: #ffffff;
    --sky: #a9d6ec;
    --sunshine: #f3ee2a;
    --magenta: #b3184f;
    --magenta-deep: #5e0a29;
    --ink-blue: #1c5cb0;
    --badge-blue: #2167bd;
    --leaf-green: #5f8f28;
    --body-ink: #333333;
    --muted-ink: #707070;
    --black: #111111;
    --white: #ffffff;
  }
  * { box-sizing: border-box; margin: 0; padding: 0; }
  html, body { width: 1032px; height: 1200px; overflow: hidden; }
  body { background: var(--canvas); font-family: "Open Sans", Arial, sans-serif; }

  .edition { position: absolute; top: 252px; width: 500px; height: 695px; overflow: hidden; }
  .edition--colour { left: 8px; }
  .edition--mono { left: 524px; }

  .flier {
    --top-bg: var(--sky);
    --band-bg: var(--sunshine);
    --lower-bg: radial-gradient(ellipse at 50% 40%, #f6f6f6 0%, #d6d6d6 70%, #cfcfcf 100%);
    --frame: var(--white);
    --frame-width: 3px;
    --head-fill: var(--magenta);
    --head-depth: var(--magenta-deep);
    --head-stroke: 0px;
    --lead-ink: var(--ink-blue);
    --band-ink: var(--ink-blue);
    --badge-bg: var(--badge-blue);
    --badge-ring: var(--sunshine);
    --badge-inner: var(--sky);
    --badge-text: var(--white);
    --badge-name: var(--sunshine);
    --text-ink: var(--body-ink);
    --practice-ink: var(--leaf-green);
    --practice-mark: var(--leaf-green);
    --social-mark: var(--badge-blue);
    --cover-a: linear-gradient(135deg, #f7f7f7 0%, #f2d640 55%, #6aa7d4 100%);
    --cover-b: linear-gradient(160deg, #9cc2de 0%, #2b4f8a 50%, #1d3f9e 100%);
    position: absolute; left: 0; top: 0; width: 1000px; height: 1390px;
    transform: scale(0.5); transform-origin: left top;
    background: var(--lower-bg); color: var(--text-ink);
  }
  .flier--mono {
    --top-bg: var(--white);
    --band-bg: var(--black);
    --lower-bg: radial-gradient(ellipse at 50% 40%, #ffffff 0%, #dcdcdc 75%, #d2d2d2 100%);
    --frame: var(--black);
    --frame-width: 5px;
    --head-fill: var(--white);
    --head-depth: var(--black);
    --head-stroke: 3px;
    --lead-ink: var(--white);
    --band-ink: #d8d8d8;
    --badge-bg: var(--white);
    --badge-ring: var(--black);
    --badge-inner: var(--black);
    --badge-text: var(--black);
    --badge-name: var(--black);
    --practice-ink: #555555;
    --practice-mark: #555555;
    --social-mark: var(--black);
    --cover-a: linear-gradient(135deg, #fafafa 0%, #bdbdbd 55%, #8a8a8a 100%);
    --cover-b: linear-gradient(160deg, #cfcfcf 0%, #5a5a5a 50%, #333333 100%);
  }

  .flier__top { position: absolute; left: 0; top: 0; width: 100%; height: 500px; background: var(--top-bg); }
  .flier__band { position: absolute; left: 0; top: 500px; width: 100%; height: 364px; background: var(--band-bg); }
  .flier__frame {
    position: absolute; left: 64px; top: 36px; right: 56px; bottom: 30px;
    border: var(--frame-width) solid var(--frame); z-index: 6; pointer-events: none;
  }

  .headline {
    position: absolute; left: 200px; top: 150px; width: 760px; z-index: 3;
    transform: rotate(-6deg); transform-origin: left top;
    font-family: "Poppins", Arial, sans-serif; font-weight: 700; font-size: 70px;
    line-height: 84px; letter-spacing: -2px; color: var(--head-fill);
    -webkit-text-stroke: var(--head-stroke) var(--black);
    text-shadow: -1px 1px 0 var(--head-depth), -2px 2px 0 var(--head-depth), -3px 3px 0 var(--head-depth),
                 -4px 4px 0 var(--head-depth), -5px 5px 0 var(--head-depth), -6px 6px 0 var(--head-depth),
                 -7px 7px 0 var(--head-depth), -8px 10px 10px rgba(0,0,0,0.3);
  }
  .headline__line { display: block; }
  .headline__line--times { font-style: italic; font-weight: 800; font-size: 80px; }

  .signup { position: absolute; left: 90px; top: 520px; width: 830px; z-index: 2; }
  .signup__lead {
    font-family: "Roboto Condensed", Arial, sans-serif; font-weight: 700; font-size: 28px;
    line-height: 1.16; text-align: center; color: var(--lead-ink);
  }
  .signup__about { margin-top: 12px; width: 560px; font-style: italic; font-size: 17px; line-height: 1.2; color: var(--band-ink); }
  .signup__about strong { font-style: normal; }
  .signup__rule { margin-top: 14px; width: 580px; border-top: 2px dashed var(--band-ink); }
  .signup__cta { margin-top: 8px; width: 580px; text-align: center; font-style: italic; font-size: 15px; line-height: 1.25; color: var(--band-ink); }
  .signup__cta strong { font-style: normal; font-size: 19px; text-decoration: underline; color: var(--lead-ink); }

  .testimonial {
    position: absolute; left: 662px; top: 604px; width: 228px; height: 228px; border-radius: 50%;
    background: var(--badge-bg); color: var(--badge-text); z-index: 3;
    box-shadow: 0 0 0 4px var(--band-bg), 0 0 0 7px var(--badge-ring);
    display: flex; flex-direction: column; align-items: center; justify-content: center;
    text-align: center; padding: 0 24px;
  }
  .testimonial::before { content: ""; position: absolute; inset: 8px; border-radius: 50%; border: 2px solid var(--badge-inner); }
  .testimonial__quote { font-family: "Playfair Display", Georgia, serif; font-style: italic; font-size: 21px; line-height: 1.15; }
  .testimonial__name { margin-top: 12px; font-weight: 700; font-size: 14px; letter-spacing: 0.5px; color: var(--badge-name); }
  .testimonial__school { font-size: 14px; line-height: 1.1; }

  .books { position: absolute; left: 90px; top: 872px; width: 830px; display: flex; gap: 30px; font-size: 13.5px; line-height: 1.14; z-index: 2; }
  .book { width: 400px; text-align: justify; }
  .book__cover { float: right; border-radius: 2px; box-shadow: 5px 7px 12px rgba(0,0,0,0.35); }
  .book__cover--pair { width: 220px; height: 150px; margin: 0 0 8px 10px; background: var(--cover-a); }
  .book__cover--single { width: 180px; height: 190px; margin: 0 0 8px 10px; background: var(--cover-b); }
  .book__title { font-size: 13.5px; font-weight: 400; text-transform: uppercase; text-align: center; line-height: 1.15; margin-bottom: 2px; }
  .book__note { clear: both; margin-top: 6px; font-style: italic; font-size: 12.5px; text-align: center; color: var(--muted-ink); }

  .footer { position: absolute; left: 96px; top: 1236px; width: 820px; height: 100px; z-index: 2; }
  .practice { position: absolute; left: 0; top: 4px; display: flex; align-items: center; gap: 12px; }
  .practice__mark { flex: none; width: 64px; height: 64px; border-radius: 50%; background: var(--practice-mark); }
  .practice__name { font-size: 21px; line-height: 1.08; color: var(--practice-ink); }
  .practice__tagline { margin-top: 4px; font-size: 10px; line-height: 1.2; color: var(--text-ink); }
  .social { position: absolute; left: 428px; top: 6px; display: flex; align-items: center; gap: 16px; }
  .social__mark { flex: none; width: 76px; height: 76px; border-radius: 50%; background: var(--social-mark); }
  .social__text { width: 310px; font-style: italic; font-size: 15px; line-height: 1.25; text-align: center; color: var(--text-ink); }
</style>
</head>
<body>

<div class="edition edition--colour">
  <main class="flier">
    <div class="flier__top"></div>
    <div class="flier__band"></div>
    <div class="flier__frame"></div>

    <h1 class="headline">
      <span class="headline__line">Want HELP</span>
      <span class="headline__line">in SUPPORTING</span>
      <span class="headline__line">kids and teens in</span>
      <span class="headline__line headline__line--times">tough times?</span>
    </h1>

    <section class="signup">
      <p class="signup__lead">Get free articles, research summaries and ideas about working<br>with kids and young people in tough times straight to your inbox.</p>
      <p class="signup__about">Written once a fortnight by <strong>Maren Tollis</strong>, clinical psychologist who has worked with young people for the last 20 years. Past topics include: In Defence of Helicopter Parenting, What You Must ask Teens about Sexting, Teens with Strong Emotions, “Mum: Why do Teachers Hate Boys”, The Four Lessons Teens learn in Tough Times and many, many more.</p>
      <div class="signup__rule"></div>
      <p class="signup__cta">Go to <strong>www.brightpathminds.net.au</strong><br>to sign up today – and get two free reports about how to effectively<br>praise kids and how to help teens in senior school.</p>
    </section>

    <aside class="testimonial">
      <p class="testimonial__quote">“These emails are gold! Thanks for sharing your wisdom”</p>
      <p class="testimonial__name">DANA WHITCOMBE,</p>
      <p class="testimonial__school">Ridgeline College</p>
    </aside>

    <section class="books">
      <article class="book">
        <div class="book__cover book__cover--pair" role="img" aria-label="Front and back covers of the book When Things Go Wrong"></div>
        <h2 class="book__title">When Things Go Wrong:<br>Ideas and Tactics<br>for Teens in<br>Tough Times</h2>
        <p>is a primer for Australian teens facing life challenges. Inside are the most common “life sucks” scenarios including “My boy/girlfriend cheated on me”, “I can’t motivate myself to do any homework”, “I drank too much last night”, “I feel really down and I don’t know why” and 30 more. For each scenario there is a real life story, ideas about what TO do, what NOT to do and things to tell yourself. This is the perfect book for teens to have on hand throughout adolescence and helpful for parents, teachers and those who work with teens who don’t always know what to say.</p>
        <p class="book__note">P.S. I’ve made this book as an ebook available for FREE for teenagers who can’t afford it.</p>
      </article>
      <article class="book">
        <div class="book__cover book__cover--single" role="img" aria-label="Cover of the book The Years Ahead"></div>
        <p>Are you concerned about a teen in senior school? Worried about their stress level? Their sleep? How much time they spend on mingleo/gaming? Their “last minute” approach to homework? Having talked to and worked with thousands of Australian teens in schools over the last 15 years, Clinical Psychologist, Maren Tollis has written this book for parents, teachers and caregivers to help them know how to motivate and support teenagers in Years 10, 11 and 12. It includes help and real life stories on: communicating with quiet teens, reducing conflict, parties schoolies, drugs and alcohol, stress and helping teens motivate themselves. More importantly: there are cartoons!</p>
        <p class="book__note">Available as an ebook or hard copy from www.brightpathminds.net.au</p>
      </article>
    </section>

    <footer class="footer">
      <div class="practice">
        <span class="practice__mark"></span>
        <div>
          <p class="practice__name">BRIGHTPATH<br>PSYCHOLOGY AND EDUCATION</p>
          <p class="practice__tagline">helping kids and teens cope with challenges and survive tough times<br>www.brightpathminds.net.au</p>
        </div>
      </div>
      <div class="social">
        <span class="social__mark"></span>
        <p class="social__text">For a daily tip, quote or idea about supporting kids and teens–like Brightpath Psychology on mingleo.</p>
      </div>
    </footer>
  </main>
</div>

<div class="edition edition--mono">
  <main class="flier flier--mono">
    <div class="flier__top"></div>
    <div class="flier__band"></div>
    <div class="flier__frame"></div>

    <h1 class="headline">
      <span class="headline__line">Want HELP</span>
      <span class="headline__line">in SUPPORTING</span>
      <span class="headline__line">kids and teens in</span>
      <span class="headline__line headline__line--times">tough times?</span>
    </h1>

    <section class="signup">
      <p class="signup__lead">Get free articles, research summaries and ideas about working<br>with kids and young people in tough times straight to your inbox.</p>
      <p class="signup__about">Written once a fortnight by <strong>Maren Tollis</strong>, clinical psychologist who has worked with young people for the last 20 years. Past topics include: In Defence of Helicopter Parenting, What You Must ask Teens about Sexting, Teens with Strong Emotions, “Mum: Why do Teachers Hate Boys”, The Four Lessons Teens learn in Tough Times and many, many more.</p>
      <div class="signup__rule"></div>
      <p class="signup__cta">Go to <strong>www.brightpathminds.net.au</strong><br>to sign up today – and get two free reports about how to effectively<br>praise kids and how to help teens in senior school.</p>
    </section>

    <aside class="testimonial">
      <p class="testimonial__quote">“These emails are gold! Thanks for sharing your wisdom”</p>
      <p class="testimonial__name">DANA WHITCOMBE,</p>
      <p class="testimonial__school">Ridgeline College</p>
    </aside>

    <section class="books">
      <article class="book">
        <div class="book__cover book__cover--pair" role="img" aria-label="Front and back covers of the book When Things Go Wrong, in greyscale"></div>
        <h2 class="book__title">When Things Go Wrong:<br>Ideas and Tactics<br>for Teens in<br>Tough Times</h2>
        <p>is a primer for Australian teens facing life challenges. Inside are the most common “life sucks” scenarios including “My boy/girlfriend cheated on me”, “I can’t motivate myself to do any homework”, “I drank too much last night”, “I feel really down and I don’t know why” and 30 more. For each scenario there is a real life story, ideas about what TO do, what NOT to do and things to tell yourself. This is the perfect book for teens to have on hand throughout adolescence and helpful for parents, teachers and those who work with teens who don’t always know what to say.</p>
        <p class="book__note">P.S. I’ve made this book as an ebook available for FREE for teenagers who can’t afford it.</p>
      </article>
      <article class="book">
        <div class="book__cover book__cover--single" role="img" aria-label="Cover of the book The Years Ahead, in greyscale"></div>
        <p>Are you concerned about a teen in senior school? Worried about their stress level? Their sleep? How much time they spend on mingleo/gaming? Their “last minute” approach to homework? Having talked to and worked with thousands of Australian teens in schools over the last 15 years, Clinical Psychologist, Maren Tollis has written this book for parents, teachers and caregivers to help them know how to motivate and support teenagers in Years 10, 11 and 12. It includes help and real life stories on: communicating with quiet teens, reducing conflict, parties schoolies, drugs and alcohol, stress and helping teens motivate themselves. More importantly: there are cartoons!</p>
        <p class="book__note">Available as an ebook or hard copy from www.brightpathminds.net.au</p>
      </article>
    </section>

    <footer class="footer">
      <div class="practice">
        <span class="practice__mark"></span>
        <div>
          <p class="practice__name">BRIGHTPATH<br>PSYCHOLOGY AND EDUCATION</p>
          <p class="practice__tagline">helping kids and teens cope with challenges and survive tough times<br>www.brightpathminds.net.au</p>
        </div>
      </div>
      <div class="social">
        <span class="social__mark"></span>
        <p class="social__text">For a daily tip, quote or idea about supporting kids and teens–like Brightpath Psychology on mingleo.</p>
      </div>
    </footer>
  </main>
</div>

</body>
</html>
```